Harbor Compass - Book Cover

I need a book cover for my debut work, "Harbor Compass - Turning the Tide, One Step at a Time." While the website isn't complete, you can get a sense of what I am writing about by looking at my website, harborcompassbooks.org. The book is a leadership development book, but more of a personal change journey. The emphasis is on figuring out how to combine you work, social, and own self into an authentic package that not only resonates with others, but makes what you achieve more fulfilling.

I am attaching a copy of my logo so you can get a sense of what I like. I would prefer to not have the cover be photographic, but am open to suggestions. This will be a series of books so maintaining some sense of style will be important, and can garner future work.

Industry/Entity Type

Leadership

```html
<!DOCTYPE html>
<html lang="en">
<head>
<meta charset="utf-8">
<title>Harbor Compass – Book Cover</title>
<link rel="stylesheet" href="https://fonts.googleapis.com/css2?family=Bebas+Neue&family=Source+Sans+3:wght@400;500&display=swap">
<style>
  :root {
    --backdrop: #e4e3e1;
    --cover: #f3f3f1;
    --cover-edge: #e2e2df;
    --author-blue: #1d4f9e;
    --title-band: #6b6b6b;
    --title-text: #efefed;
    --subtitle-band: #1c55a9;
    --subtitle-text: #ffffff;
    --stone-light: #d2d1ce;
    --stone-mid: #a9a8a5;
    --stone-dark: #8a8986;
  }
  * { margin: 0; padding: 0; box-sizing: border-box; }
  html, body {
    width: 1200px;
    height: 1000px;
    overflow: hidden;
    background: var(--backdrop);
  }
  .canvas {
    position: relative;
    width: 1200px;
    height: 1000px;
  }
  .book-cover {
    position: absolute;
    left: 340px;
    top: 113px;
    width: 545px;
    height: 775px;
    background: linear-gradient(90deg, var(--cover-edge) 0, var(--cover) 14px, var(--cover) 100%);
    box-shadow: 0 4px 18px rgba(0,0,0,0.12);
    overflow: hidden;
  }
  .author-name {
    position: absolute;
    top: 58px;
    left: 0;
    width: 100%;
    text-align: center;
    font-family: "Bebas Neue", "Oswald", sans-serif;
    font-size: 66px;
    letter-spacing: 1px;
    line-height: 1;
    color: var(--author-blue);
  }
  .stone-stack {
    position: absolute;
    left: 130px;
    top: 172px;
    width: 305px;
    height: 545px;
  }
  .title-band {
    position: absolute;
    left: 53px;
    top: 212px;
    width: 442px;
    height: 86px;
    background: var(--title-band);
    transform: rotate(-3deg);
    display: flex;
    align-items: center;
    justify-content: center;
    font-family: "Source Sans 3", "Source Sans Pro", sans-serif;
    font-weight: 400;
    font-size: 52px;
    color: var(--title-text);
    box-shadow: 0 2px 4px rgba(0,0,0,0.15);
  }
  .subtitle-band {
    position: absolute;
    left: 70px;
    top: 318px;
    width: 408px;
    height: 68px;
    background: var(--subtitle-band);
    transform: rotate(2deg);
    display: flex;
    flex-direction: column;
    align-items: center;
    justify-content: center;
    font-family: "Source Sans 3", "Source Sans Pro", sans-serif;
    font-weight: 500;
    font-size: 22px;
    line-height: 1.1;
    color: var(--subtitle-text);
    text-align: center;
    box-shadow: 0 2px 4px rgba(0,0,0,0.15);
  }
</style>
</head>
<body>
  <main class="canvas">
    <section class="book-cover">
      <h2 class="author-name">Daniel Hale</h2>

      <svg class="stone-stack" viewBox="0 0 305 545" role="img" aria-label="Photograph of a balanced stack of smooth grey pebbles on a large flat stone">
        <defs>
          <linearGradient id="stoneTone" x1="0" y1="0" x2="0" y2="1">
            <stop offset="0" stop-color="var(--stone-mid)"/>
            <stop offset="0.5" stop-color="var(--stone-dark)"/>
            <stop offset="1" stop-color="var(--stone-light)"/>
          </linearGradient>
        </defs>
        <path d="M80 12 Q150 -4 212 12 Q220 40 190 60 L200 240 Q230 330 240 420 Q300 450 300 500 Q270 545 150 540 Q10 545 5 500 Q10 455 70 420 Q80 330 110 240 L118 60 Q74 40 80 12 Z" fill="url(#stoneTone)" opacity="0.85"/>
      </svg>

      <h1 class="title-band">Harbor Compass</h1>
      <p class="subtitle-band">
        <span>Turning the Tide,</span>
        <span>One Step at a Time</span>
      </p>
    </section>
  </main>
</body>
</html>
```